Flooring Company Wordpress Design Using Elementor

We need a website design using elementor for a flooring company. I have attached a word document with the entire content for the site. I have sample websites www.pellmarbuildersnevada.com and www.tilbrookfinishesreno.com

The site needs to look alot better than the samples. Modern and professional is what we are looking for. 100 times better than the sample websites.

I have images to be used in the site but the file is to large to attached here.

```html
<!DOCTYPE html>
<html lang="en">
<head>
<meta charset="utf-8">
<title>Keystone Flooring</title>
<link href="https://fonts.googleapis.com/css2?family=Lato:wght@400;700;900&display=swap" rel="stylesheet">
<style>
:root{
  --red:#d0111b;
  --red-dark:#a80d15;
  --ink:#1d1d1d;
  --text:#555;
  --muted:#8a8a8a;
  --line:#dcdcdc;
  --light:#f4f4f4;
  --dark:#1f1f1f;
  --white:#fff;
}
*{box-sizing:border-box;margin:0;padding:0}
html,body{width:1200px;height:4896px;overflow:hidden}
body{font-family:'Lato',sans-serif;color:var(--text);background:var(--white);position:relative}
.section{position:absolute;left:0;width:1200px}
.btn{display:inline-block;font-weight:700;font-size:14px;letter-spacing:.5px;padding:12px 24px;text-transform:uppercase}
.btn-red{background:var(--red);color:var(--white)}
.btn-outline-white{border:2px solid var(--white);color:var(--white)}
.btn-outline-red{border:2px solid var(--red);color:var(--red)}
.btn-dark{background:#3a3a3a;color:var(--white)}
p{font-size:15px;line-height:1.55}

/* header / hero */
.hero{top:0;height:610px;background:linear-gradient(135deg,#8a7a6a 0%,#5b4f46 45%,#7f7b77 75%,#47433f 100%)}
.hero-shade{position:absolute;inset:0;background:linear-gradient(90deg,rgba(0,0,0,.55),rgba(0,0,0,.1))}
.topbar{position:absolute;top:0;left:0;right:0;height:70px;display:flex;align-items:center;padding:0 36px}
.logo{font-weight:900;font-size:26px;color:var(--white);line-height:1}
.logo-mark{display:inline-block;width:14px;height:14px;background:var(--red);margin-right:8px}
.nav{margin-left:auto;display:flex;align-items:stretch;height:70px}
.nav a{display:flex;align-items:center;padding:0 22px;color:var(--white);font-weight:700;font-size:15px;text-decoration:none}
.nav a.active{background:var(--red)}
.nav .search{padding:0 10px}
.hero-copy{position:absolute;left:170px;top:205px;width:560px;color:var(--white)}
.hero-copy h1{font-size:42px;font-weight:900;line-height:1.12;text-transform:uppercase}
.hero-copy .rule{width:80px;height:4px;background:var(--red);margin:16px 0}
.hero-copy p{color:#eee;font-size:15px}
.hero-actions{margin-top:34px;display:flex;gap:16px}

/* features */
.features{top:610px;height:530px;display:flex;justify-content:center;gap:60px;padding-top:70px}
.feature{width:300px;text-align:center}
.feature svg{width:64px;height:64px}
.feature h3{color:var(--ink);font-size:17px;font-weight:900;margin:18px 0 14px;text-transform:uppercase;line-height:1.3}
.feature p{text-align:justify;font-size:14px}

/* partner */
.partner{top:1140px;height:440px;display:flex}
.partner-copy{width:600px;background:var(--red);color:var(--white);padding:60px 60px 0 130px}
.partner-copy h2{font-size:34px;font-weight:900;line-height:1.15;text-transform:uppercase}
.partner-copy .rule{width:70px;height:4px;background:var(--white);margin:14px 0}
.partner-copy p{font-size:15px;color:#fbe6e6}
.partner-copy .btn{margin-top:26px}
.partner-photo{flex:1;background:linear-gradient(140deg,#3b342f,#6f5c4d 45%,#a68e74 70%,#4b4038)}

/* services */
.services{top:1580px;height:880px;text-align:center;padding-top:58px}
.eyebrow{font-weight:900;color:var(--ink);font-size:16px;text-transform:uppercase}
.services h2{font-size:36px;font-weight:900;color:var(--red);line-height:1.15;margin-top:6px;text-transform:uppercase}
.cards{display:flex;justify-content:center;gap:40px;margin-top:50px}
.card{width:280px;text-align:left}
.card-photo{height:210px}
.card h3{color:var(--red);font-size:16px;font-weight:900;margin:22px 0 10px;text-transform:uppercase}
.card p{font-size:14px;text-align:justify}
.card-actions{display:flex;gap:10px;margin-top:18px}
.card-actions .btn{padding:10px 14px;font-size:12px}
.view-all{margin-top:40px;font-weight:700;font-size:16px;color:var(--red);display:flex;align-items:center;justify-content:center;gap:12px}
.view-all span{border-bottom:2px solid var(--red)}
.dots{display:flex;justify-content:center;gap:8px;margin-top:20px}
.dots i{width:8px;height:8px;border-radius:50%;background:#ccc}
.dots i.on{background:var(--red)}

/* testimonials */
.testimonials{top:2460px;height:400px;background:linear-gradient(120deg,#6a5d50,#3e3731 50%,#5a4e43);text-align:center;color:var(--white);padding-top:60px}
.testimonials::before{content:"";position:absolute;inset:0;background:rgba(0,0,0,.55)}
.testimonials > *{position:relative}
.testimonials h2{font-size:34px;font-weight:900;text-transform:uppercase}
.quote{color:var(--red);font-size:70px;font-weight:900;line-height:.8;margin-top:18px}
.testimonials p{width:820px;margin:10px auto 0;font-size:13px;color:#e5e5e5}
.avatar{width:70px;height:70px;border-radius:50%;background:#c8a68c;margin:22px auto 0;border:3px solid var(--white)}
.client{color:var(--red);font-weight:700;font-size:13px;margin-top:8px;text-transform:uppercase}
.testimonials .arrow{position:absolute;top:190px}
.testimonials .arrow.left{left:90px}
.testimonials .arrow.right{left:auto;right:90px}

/* process */
.process{top:2860px;height:720px;background:var(--light);text-align:center;padding-top:60px}
.process h2{font-size:34px;font-weight:900;color:var(--red);text-transform:uppercase}
.steps-line{position:absolute;top:228px;left:200px;width:800px;height:2px;background:var(--line)}
.steps{display:flex;justify-content:center;gap:40px;margin-top:95px}
.step{width:180px;position:relative}
.step .num{width:70px;height:70px;border-radius:50%;background:#444;color:var(--white);font-weight:900;font-size:24px;display:flex;align-items:center;justify-content:center;margin:0 auto;border:6px solid var(--white);box-shadow:0 0 0 2px var(--line)}
.step-box{background:var(--white);box-shadow:0 4px 14px rgba(0,0,0,.08);margin-top:26px;padding:22px 16px;min-height:250px}
.step h3{color:var(--red);font-size:14px;font-weight:900;text-transform:uppercase;line-height:1.35}
.step p{font-size:13px;margin-top:14px}
.process .btn{margin-top:50px;padding:10px 30px}

/* contact */
.contact{top:3580px;height:740px;background:linear-gradient(150deg,#4a3a2c,#8a6a4c 40%,#c9a47c 60%,#5c4533)}
.contact-panel{position:absolute;left:200px;top:90px;width:800px;height:560px;background:rgba(255,255,255,.93);padding:40px 60px;text-align:center}
.contact-panel h2{color:var(--red);font-size:34px;font-weight:900;text-transform:uppercase}
.contact-panel .rule{width:60px;height:3px;background:var(--red);margin:10px auto 30px}
.fields{display:grid;grid-template-columns:1fr 1fr;gap:18px 30px}
.field{border:1px solid var(--line);background:var(--white);height:46px;text-align:left;padding:14px;font-size:13px;color:var(--muted)}
.field.wide{grid-column:1/3;height:150px}
.contact-panel .btn{margin-top:30px;padding:12px 40px}

/* footer */
.footer{top:4320px;height:576px;background:var(--dark);color:#bbb}
.footer-cols{display:flex;gap:50px;padding:70px 90px 0}
.footer h4{color:var(--white);font-size:22px;font-weight:700;margin-bottom:20px}
.footer p,.footer li{font-size:14px;line-height:1.6}
.f-brand{width:230px}
.f-brand .logo{margin-bottom:20px}
.socials{display:flex;gap:10px;margin-top:20px}
.socials i{width:28px;height:28px;border-radius:50%;background:#555}
.f-links{width:170px}
.f-links ul{list-style:none}
.f-links li::before{content:"";display:inline-block;width:6px;height:6px;background:var(--red);margin-right:10px;vertical-align:middle}
.f-news{width:290px}
.news-item{display:flex;gap:12px;margin-bottom:16px;align-items:center}
.news-item .thumb{width:48px;height:48px;border-radius:50%;background:#6b5b4c;flex:none}
.footer .news-item p{font-size:13px;line-height:1.4}
.f-contact{width:220px}
.copyright{position:absolute;bottom:0;left:0;right:0;height:60px;border-top:1px solid #333;display:flex;align-items:center;justify-content:center;font-size:13px;color:#999}
</style>
</head>
<body>

<section class="section hero" role="img" aria-label="Photo of a bright modern kitchen with tiled flooring">
  <div class="hero-shade"></div>
  <header class="topbar">
    <div class="logo"><span class="logo-mark"></span>Keystone Flooring</div>
    <nav class="nav">
      <a class="active">HOME</a><a>ABOUT US</a><a>SERVICES</a><a>BLOGS</a><a>CONTACT US</a>
      <a class="search"><svg width="18" height="18" viewBox="0 0 20 20"><circle cx="8" cy="8" r="6" fill="none" stroke="#d0111b" stroke-width="2.5"/><line x1="12.5" y1="12.5" x2="18" y2="18" stroke="#d0111b" stroke-width="2.5"/></svg></a>
    </nav>
  </header>
  <div class="hero-copy">
    <h1>Change your building flooring story with Keystone Group</h1>
    <div class="rule"></div>
    <p>We transform homes and businesses with lasting floors. Choose from our trusted range of products and let our team handle every step of your project.</p>
    <div class="hero-actions"><span class="btn btn-dark">Explore</span><span class="btn btn-red">Free Estimate</span></div>
  </div>
</section>

<section class="section features">
  <div class="feature">
    <svg viewBox="0 0 64 64" fill="none" stroke="#1d1d1d" stroke-width="2"><circle cx="32" cy="32" r="30"/><circle cx="32" cy="26" r="9"/><path d="M18 48c2-8 8-12 14-12s12 4 14 12"/></svg>
    <h3>Minimal stress on<br>your plate</h3>
    <p>Floor installation or removal can be stressful for both parties. You have to relocate most of your property on the affected area to a new location and adjust your daily operation. The last thing we want to do is add to that. Hence, we take a proactive, customer-focused approach on all our floor installation. We will assist you with your property relocation and cleaning, and ensure a quick and smooth process.</p>
  </div>
  <div class="feature">
    <svg viewBox="0 0 64 64" fill="none" stroke="#1d1d1d" stroke-width="2"><circle cx="32" cy="32" r="30"/><path d="M16 34l16-14 16 14M21 30v16h22V30"/><rect x="28" y="36" width="8" height="10"/></svg>
    <h3>A floor worthy<br>of your home</h3>
    <p>The quality and type of your floor are as important as its style and appeal. The wrong combination could see you spending a lot on maintenance and feeling frustrated. That's why here at Keystone Group, don't just go with what is available, but what fits best. We will work with you to identify the kind of floor that matches your lifestyle, fitness preference, and strikes a balance between cost, maintenance and durability.</p>
  </div>
  <div class="feature">
    <svg viewBox="0 0 64 64" fill="none" stroke="#1d1d1d" stroke-width="2"><circle cx="32" cy="32" r="30"/><rect x="18" y="18" width="28" height="22"/><circle cx="32" cy="43" r="6"/><path d="M28 48l-2 8 6-3 6 3-2-8"/></svg>
    <h3>Qualified and<br>certified experts</h3>
    <p>After spending a lot to finally get that property of your dream, the last thing you want is some rookie messing it up and getting you back on your plans. Here at Keystone Group we understand this and strive to avoid its occurrence. Hence, we never assign your projects to unvetted professionals. Our team of experts is made up of only highly experienced and passionate individuals licensed in their specific fields to ensure the best results possible.</p>
  </div>
</section>

<section class="section partner">
  <div class="partner-copy">
    <h2>A reliable<br>partner to lean on</h2>
    <div class="rule"></div>
    <p>Keystone Group comes with over 14 years of experience in floor installation. We are specialists when it comes to the installation hardwood installation, carpet installation, tile backsplash installation, vinyl installation, laminate floor installation, and floor removal. Over the years, we have come to position ourselves as the professional hands our customers need for all.</p>
    <span class="btn btn-outline-white">Learn More</span>
  </div>
  <div class="partner-photo" role="img" aria-label="Photo of a modern living room with a patterned area rug and wooden floor"></div>
</section>

<section class="section services">
  <div class="eyebrow">Our Services</div>
  <h2>Make your floors scream<br>quality and beauty</h2>
  <div class="cards">
    <div class="card">
      <div class="card-photo" role="img" aria-label="Photo of a bathroom with grey floor tiles" style="background:linear-gradient(135deg,#d9d6d0,#a9a49c)"></div>
      <h3>Tile Installation</h3>
      <p>Tile is one durable flooring material that, when placed well, leaves your home or property looking luxurious and inviting. Keystone Group is fitted with expert tile installers who have experience installing anything tile, from the flooring, bathroom tile, to backsplash tile. Allow us to make</p>
      <div class="card-actions"><span class="btn btn-outline-red">Learn More</span><span class="btn btn-red">Get Free Quote</span></div>
    </div>
    <div class="card">
      <div class="card-photo" role="img" aria-label="Photo of an installer laying hardwood planks" style="background:linear-gradient(135deg,#c08a5a,#7a5233)"></div>
      <h3>Hardwood Installation</h3>
      <p>Tile is one durable flooring material that, when placed well, leaves your home or property looking luxurious and inviting. Keystone Group is fitted with expert tile installers who have experience installing anything tile, from the flooring, bathroom tile, to backsplash tile. Allow us to make</p>
      <div class="card-actions"><span class="btn btn-outline-red">Learn More</span><span class="btn btn-red">Get Free Quote</span></div>
    </div>
    <div class="card">
      <div class="card-photo" role="img" aria-label="Photo of laminate planks being fitted" style="background:linear-gradient(135deg,#b59a7e,#6e5a48)"></div>
      <h3>Laminate Installation</h3>
      <p>Tile is one durable flooring material that, when placed well, leaves your home or property looking luxurious and inviting. Keystone Group is fitted with expert tile installers who have experience installing anything tile, from the flooring, bathroom tile, to backsplash tile. Allow us to make</p>
      <div class="card-actions"><span class="btn btn-outline-red">Learn More</span><span class="btn btn-red">Get Free Quote</span></div>
    </div>
  </div>
  <div class="view-all"><span>View All Services</span><svg width="30" height="12" viewBox="0 0 30 12"><path d="M0 6h27M22 1l6 5-6 5" fill="none" stroke="#d0111b" stroke-width="2"/></svg></div>
  <div class="dots"><i class="on"></i><i></i><i></i></div>
</section>

<section class="section testimonials" role="img" aria-label="Photo of a furnished room with wooden flooring behind the testimonials">
  <h2>Clients Testimonials</h2>
  <div class="quote">&ldquo;</div>
  <p>Keystone fitted our new floors in under a week and left every room spotless. The team explained each option clearly, kept to the agreed budget and arrived on time every single day. Our living room and hallway now look brand new and the finish has held up perfectly. We will gladly call them again for our next project.</p>
  <div class="avatar" role="img" aria-label="Client portrait"></div>
  <div class="client">Laura Bennett</div>
  <svg class="arrow left" width="20" height="34" viewBox="0 0 20 34"><path d="M17 2L3 17l14 15" fill="none" stroke="#fff" stroke-width="3"/></svg>
  <svg class="arrow right" width="20" height="34" viewBox="0 0 20 34"><path d="M3 2l14 15L3 32" fill="none" stroke="#fff" stroke-width="3"/></svg>
</section>

<section class="section process">
  <h2>A simple, repeatable process</h2>
  <div class="steps-line"></div>
  <div class="steps">
    <div class="step"><div class="num">1</div><div class="step-box"><h3>Schedule an appointment</h3><p>Fill out the form on our site or call us today for free to relax your week, and schedule a free site inspection. It is that simple!</p></div></div>
    <div class="step"><div class="num">2</div><div class="step-box"><h3>Your preferred floor material</h3><p>Based on our findings on consultation and our inspection, we will help you figure out the right type of floor for your home or business space.</p></div></div>
    <div class="step"><div class="num">3</div><div class="step-box"><h3>Premium installation</h3><p>After the two stages are done, and you have approved the work date, our professionals for your floor will begin work on your property.</p></div></div>
    <div class="step"><div class="num">4</div><div class="step-box"><h3>A happy you</h3><p>With a quality job done, go ahead and enjoy your floors for years to come with minimal maintenance on your side!</p></div></div>
  </div>
  <span class="btn btn-outline-red">Explore</span>
</section>

<section class="section contact" role="img" aria-label="Photo of a kitchen with warm hardwood flooring">
  <div class="contact-panel">
    <h2>Contact Us</h2>
    <div class="rule"></div>
    <div class="fields">
      <div class="field">Name</div><div class="field">Phone</div>
      <div class="field">Email</div><div class="field">Appointment Date</div>
      <div class="field wide">Message</div>
    </div>
    <span class="btn btn-red">Submit</span>
  </div>
</section>

<footer class="section footer">
  <div class="footer-cols">
    <div class="f-brand">
      <div class="logo"><span class="logo-mark"></span>Keystone Flooring</div>
      <p>We are family owned and trusted builders for a number of great care points and people. Our experience has taken us from small to large projects.</p>
      <div class="socials"><i></i><i></i><i></i><i></i><i></i></div>
    </div>
    <div class="f-links">
      <h4>Explor link</h4>
      <ul><li>Home</li><li>About Us</li><li>Our services</li><li>Meet our team</li><li>Webpage</li><li>Contact</li><li>Privacy Policy</li></ul>
    </div>
    <div class="f-news">
      <h4>Latest News</h4>
      <div class="news-item"><div class="thumb" role="img" aria-label="News thumbnail"></div><p>Choosing hardwood for busy family homes</p></div>
      <div class="news-item"><div class="thumb" role="img" aria-label="News thumbnail"></div><p>Tile care tips for the winter months</p></div>
      <div class="news-item"><div class="thumb" role="img" aria-label="News thumbnail"></div><p>Laminate or vinyl: which suits your space</p></div>
      <div class="news-item"><div class="thumb" role="img" aria-label="News thumbnail"></div><p>How to prepare a room for new flooring</p></div>
    </div>
    <div class="f-contact">
      <h4>Contact us</h4>
      <p>2210 Orchard Lane, Oakridge, Florida</p>
      <p style="margin-top:14px">info@keystoneflooring.com</p>
      <p style="margin-top:14px">+1 555 014 2290<br>+1 555 014 2291</p>
    </div>
  </div>
  <div class="copyright">Copyright &copy; 2020 Keystone Flooring. All Rights Reserved</div>
</footer>

</body>
</html>
```